Purple Heart Veteran Owned Telecommunications Company

I need to develop my current website (ridgewellcore.com) into something more upbeat and modern. I created the existing one with SiteNimbo and it's very basic. I'm open to using any type of website builder and not just SiteNimbo. I feel like SiteNimbo is pretty basic. I want something customized to me and my company. I plan on doing a Brivora Ad, Email Marketing, and Mail Marketing campaign and SEO push. I want a website built so they can look up my company. We are a low voltage telecommunications company based out of Chicago. We are a General Contractor and I have technicians all throughout the US and Canada. I mainly appeal to the government and fortune 500 companies across the country. I focus on commercial and federal work with minor work in Residential. I need to appeal to everyone and not just locally. My company name is Ridgewellcore. I'm a Marine Corps veteran and my I created the company with my son in mind. We are a service disabled veteran owned small business. I'm open to any play on my logo or color scheme. I do like the color blue but I'm open to anything again. I would like a website that has little maintenance needed and something that is modern and sticks out with my competitors. I'm only in business for 2 years but I need to stick out to my competition so I can start building revenue through ads and getting my name out there with limited funds. I did have a logo and name created which I'm attaching. I'm completely open to changing it if someone can come up with something creative. I would like someone that understands SEO and can help feed work to my site. I'm also open to paying more for the right website that gets everything I want. I know I need to add more pages and more professional. Please use my website as a template but also feel free to come up with any new ideas. I would like some feedback or ideas on what else to add to my website or remove so I can appeal to my audience and look more authentic.

Target Market(s)

Commercial Companies locally in Chicago, and Fortune 500 companies and the government

Industry/Entity Type

Telecommunications

Coding

Coded - Design and coding required

Number of Pages Required

5+ page

Font styles to use
Sans Serif

Requirements
Must have
• A Modern, fresh look that is customized and original. Something that sticks out to my customers.
Nice to have
• Anything that sticks out and isn't stock. I'm open to anything that is unique and different.
Should not have
• Nothing Generic. I would like something custom tailored to my business

```html
<!DOCTYPE html>
<html lang="en">
<head>
<meta charset="utf-8">
<title>Ridgewellcore – Home Layouts</title>
<link href="https://fonts.googleapis.com/css2?family=Libre+Baskerville:wght@400;700&family=Lato:wght@400;700&display=swap" rel="stylesheet">
<style>
:root{
  --navy:#0f2c6b;
  --blue:#15407f;
  --ink:#222a38;
  --muted:#4a5160;
  --light:#e4e9f1;
  --white:#ffffff;
  --board:#7b797a;
  --black:#050505;
}
*{box-sizing:border-box;margin:0;padding:0}
html,body{width:699px;height:1200px;overflow:hidden;background:var(--board)}
.stage{position:relative;width:1468px;height:2520px;transform:scale(0.47616);transform-origin:0 0;background:var(--board)}
.page{position:absolute;top:29px;width:680px;height:2437px;background:var(--white);font-family:'Lato',sans-serif;color:var(--ink);overflow:hidden}
.page--a{left:34px}.page--b{left:750px}
section,header,footer{position:relative;width:680px}

/* header */
.site-header{height:52px;background:var(--white)}
.brand{position:absolute;left:18px;top:14px;display:flex;align-items:center;gap:7px}
.brand-dot{width:24px;height:24px;border-radius:50%;background:var(--navy)}
.brand-name{font-family:'Libre Baskerville',serif;font-size:12.5px;color:var(--navy);white-space:nowrap}
.nav{position:absolute;left:203px;top:21px;display:flex;gap:21px;font-size:8.5px;font-weight:700;color:var(--ink);letter-spacing:.2px}
.nav a{color:inherit;text-decoration:none;position:relative}
.nav a.active{color:var(--blue)}
.nav a.active::after{content:"";position:absolute;left:0;right:0;bottom:-7px;height:1px;background:var(--blue);box-shadow:0 3px 0 var(--blue)}
.phone{position:absolute;left:534px;top:13px;width:122px;height:26px;border-radius:13px;background:var(--navy);display:flex;align-items:center;padding-left:4px;gap:9px;color:var(--white);font-family:'Libre Baskerville',serif;font-size:11.5px}
.phone-ic{width:19px;height:19px;border-radius:50%;background:var(--white);display:flex;align-items:center;justify-content:center}

/* photo fills */
.ph-hero{background:
  radial-gradient(ellipse 30% 40% at 18% 45%,rgba(235,225,215,.55),transparent 70%),
  radial-gradient(ellipse 60% 35% at 60% 100%,rgba(60,90,115,.75),transparent 70%),
  linear-gradient(180deg,#9fc8d9 0%,#b7d0dc 28%,#9ab5c4 55%,#6f8fa3 80%,#55758b 100%)}
.ph-panel{background:
  radial-gradient(ellipse 40% 50% at 20% 40%,#e6ddd6,transparent 70%),
  radial-gradient(ellipse 35% 40% at 55% 30%,#e89a3c,transparent 70%),
  radial-gradient(ellipse 40% 45% at 80% 75%,#2b2b2e,transparent 75%),
  linear-gradient(135deg,#cdbba6,#c98a45 50%,#4a4038)}
.ph-rack{background:
  radial-gradient(ellipse 30% 35% at 55% 55%,#d8f1ff,transparent 70%),
  radial-gradient(ellipse 45% 50% at 20% 70%,#6fc3ee,transparent 70%),
  radial-gradient(ellipse 45% 50% at 85% 25%,#2f7fd0,transparent 70%),
  linear-gradient(135deg,#1a4fa6,#3b8fd6 50%,#123b86)}
.ph-city{background:
  radial-gradient(ellipse 40% 30% at 50% 35%,rgba(200,225,245,.7),transparent 70%),
  radial-gradient(ellipse 60% 40% at 50% 100%,#0a2445,transparent 70%),
  linear-gradient(180deg,#4f8ab7,#2a6ba3 40%,#174b80 70%,#0c2d57)}
.ph-cam{background:radial-gradient(ellipse 40% 45% at 65% 50%,#f2efe8,transparent 70%),linear-gradient(135deg,#9d9a95,#d8d2c7 50%,#a88d73)}
.ph-mall{background:radial-gradient(ellipse 50% 40% at 50% 40%,#d9c6ae,transparent 70%),linear-gradient(180deg,#8a7360,#6b4b38 60%,#3e2c22)}
.ph-dome{background:radial-gradient(ellipse 30% 45% at 45% 70%,#f0f0ee,transparent 70%),linear-gradient(180deg,#2f6fc8,#7fa8dc 50%,#d6dce4)}
.ph-retail{background:radial-gradient(ellipse 25% 40% at 90% 55%,#6e9a4a,transparent 70%),linear-gradient(180deg,#8db3e0 0%,#a9c4e2 30%,#a0614a 55%,#8a5240 80%,#9a9a98)}
.ph-servers{background:radial-gradient(ellipse 18% 60% at 50% 40%,#f5f6f8,transparent 70%),linear-gradient(90deg,#25282c,#8d9196 35%,#dcdfe2 50%,#8d9196 65%,#25282c)}
.ph-mixed{background:radial-gradient(ellipse 50% 30% at 50% 85%,#d9c9b3,transparent 70%),linear-gradient(180deg,#4f8fd8 0%,#86b0e2 30%,#b06a44 55%,#9c5a3c 80%,#c6b49c)}

/* hero */
.hero{height:341px}
.hero-photo{position:absolute;inset:0}
.hero-title{position:absolute;left:321px;top:78px;font-family:'Libre Baskerville',serif;font-weight:400;font-size:22.5px;line-height:34px;color:var(--navy);letter-spacing:.2px}
.hero-copy{position:absolute;left:321px;top:155px;width:290px;font-size:9.3px;line-height:17px;color:var(--white)}
.pill{display:flex;align-items:center;justify-content:center;border-radius:14px;background:var(--navy);color:var(--white);font-family:'Libre Baskerville',serif;font-size:10.5px;position:absolute}
.hero .pill{left:321px;top:227px;width:104px;height:27px}
.arrow{position:absolute;top:163px}

/* headings */
.h2{position:absolute;left:0;right:0;text-align:center;font-family:'Libre Baskerville',serif;font-weight:400;font-size:21px;color:var(--navy)}
.h2::after{content:"";display:block;width:52px;height:2px;background:var(--navy);margin:9px auto 0}
.on-dark .h2{color:var(--white)}
.on-dark .h2::after{background:var(--white)}

/* about */
.about{height:292px;background:var(--light)}
.about .h2{top:50px}
.about-copy{position:absolute;left:84px;width:512px;top:94px;text-align:center;font-size:8px;line-height:17px;color:var(--ink)}
.about .pill{left:288px;top:211px;width:105px;height:28px}

/* services */
.services{height:789px;background:var(--white)}
.services .h2{top:50px}
.svc{position:absolute;left:0;width:680px;height:190px}
.svc-frame{position:absolute;top:0;width:171px;height:188px;border:2px solid var(--navy);border-radius:6px}
.svc-photo{position:absolute;top:5px;width:277px;height:177px;border-radius:6px}
.svc-hex{position:absolute;top:67px;width:52px;height:54px}
.svc-title{position:absolute;top:17px;font-family:'Libre Baskerville',serif;font-weight:400;font-size:15px;color:var(--navy)}
.svc-list{position:absolute;top:49px;list-style:none;font-size:9px;color:var(--ink)}
.svc-list li{height:20.3px;display:flex;align-items:center;gap:6px;white-space:nowrap}
.tick{width:9px;height:9px;flex:none}
.outline-btn{position:absolute;top:145px;width:92px;height:24px;border:1.5px solid var(--navy);border-radius:12px;display:flex;align-items:center;justify-content:center;font-family:'Libre Baskerville',serif;font-size:8.5px;color:var(--navy)}
.svc--right .svc-frame{left:448px}.svc--right .svc-photo{left:337px}.svc--right .svc-hex{left:311px}
.svc--right .svc-title,.svc--right .svc-list,.svc--right .outline-btn{left:61px}
.svc--left .svc-frame{left:61px}.svc--left .svc-photo{left:67px}.svc--left .svc-hex{left:318px}
.svc--left .svc-title,.svc--left .svc-list,.svc--left .outline-btn{left:427px}

/* trust */
.trust{height:196px;background:radial-gradient(ellipse 70% 60% at 50% 40%,#1c4a92,transparent 80%),linear-gradient(180deg,#163f84 0%,#0f3272 60%,#0c2a63 100%)}
.trust .h2{top:50px}
.trust-copy{position:absolute;left:0;right:0;top:99px;text-align:center;font-family:'Libre Baskerville',serif;font-size:9.6px;line-height:17px;color:var(--white)}

/* markets */
.markets{height:713px;background:var(--light)}
.markets .h2{top:49px}
.card{position:absolute;width:175px;height:235px;background:var(--white);border-radius:6px;box-shadow:0 3px 10px rgba(20,40,80,.18)}
.card-photo{position:absolute;left:3px;top:3px;width:169px;height:112px;border-radius:5px 5px 0 0}
.card-title{position:absolute;left:0;right:0;top:124px;text-align:center;font-family:'Libre Baskerville',serif;font-weight:400;font-size:10.5px;color:var(--navy)}
.card-copy{position:absolute;left:14px;right:14px;top:154px;text-align:center;font-size:7.6px;line-height:17px;color:var(--muted)}
.card-link{position:absolute;left:0;right:0;top:211px;text-align:center;font-family:'Libre Baskerville',serif;font-size:7.6px;font-weight:700;color:var(--navy)}
.c1{left:65px}.c2{left:254px}.c3{left:442px}
.r1{top:106px}.r2{top:369px}
.markets .pill{left:288px;top:634px;width:105px;height:28px}

/* footer */
.site-footer{height:54px;background:var(--black);color:var(--white);font-size:7.3px;display:flex;align-items:center;justify-content:center}
</style>
</head>
<body>
<div class="stage">

  <!-- Layout A -->
  <div class="page page--a">
    <header class="site-header">
      <div class="brand"><span class="brand-dot"></span><span class="brand-name">RIDGEWELLCORE</span></div>
      <nav class="nav"><a class="active">HOME</a><a>LOW VOLTAGE</a><a>MARKETS</a><a>OUR TEAM</a><a>CONTACT US</a></nav>
      <div class="phone"><span class="phone-ic"><svg width="10" height="10" viewBox="0 0 24 24"><path fill="#0f2c6b" d="M6.6 10.8a15.1 15.1 0 0 0 6.6 6.6l2.2-2.2c.3-.3.7-.4 1-.2 1.1.4 2.3.6 3.6.6.6 0 1 .4 1 1V20c0 .6-.4 1-1 1A17 17 0 0 1 3 4c0-.6.4-1 1-1h3.5c.6 0 1 .4 1 1 0 1.3.2 2.5.6 3.6.1.3 0 .7-.2 1z"/></svg></span>555-014-2270</div>
    </header>

    <section class="hero">
      <div class="hero-photo ph-hero" role="img" aria-label="City skyline in soft blue haze with a network of hexagon photo tiles"></div>
      <svg class="arrow" style="left:14px" width="10" height="14" viewBox="0 0 10 14"><path d="M8 1 2 7l6 6" stroke="#fff" stroke-width="2" fill="none"/></svg>
      <svg class="arrow" style="left:647px" width="10" height="14" viewBox="0 0 10 14"><path d="M2 1l6 6-6 6" stroke="#fff" stroke-width="2" fill="none"/></svg>
      <h1 class="hero-title">WITH OVER 20 YEARS OF<br>PROVEN EXPERIENCE</h1>
      <p class="hero-copy">We offer an end-to-end client experience that includes seamless communication, budgeting, staffing, on-site organization, and solid, quality handiwork every time.</p>
      <span class="pill">GET STARTED</span>
    </section>

    <section class="about">
      <h2 class="h2">ABOUT RIDGEWELLCORE</h2>
      <p class="about-copy">Lorem ipsum dolor sit amet, consectetur adipiscing elit, sed do eiusmod tempor incididunt ut labore et dolore magna aliqua. Ut enim ad minim veniam, quis nostrud exercitation ullamco laboris nisi ut aliquip ex ea commodo consequat. Duis aute irure dolor in reprehenderit in voluptate velit esse cillum dolore eu fugiat nulla pariatur. Excepteur sint occaecat cupidatat non proident, sunt in culpa qui officia deserunt mollit anim id est laborum sit amet, consectetur adipiscing elit, sed do eiusmod tempor incididunt ut labore et dolore magna aliqua. Ut enim ad minim veniam, quis nostrud exercitation ullamco laboris nisi ut aliquip ex ea commodo consequat. Duis aute irure dolor in reprehenderit in voluptate velit esse cillum dolore eu fugiat nulla pariatur.</p>
      <span class="pill">LEARN MORE</span>
    </section>

    <section class="services">
      <h2 class="h2">WHAT WE DO</h2>
      <div class="svc svc--right" style="top:109px">
        <div class="svc-frame"></div>
        <div class="svc-photo ph-panel" role="img" aria-label="Technician testing an electrical panel with a clamp meter"></div>
        <svg class="svc-hex" viewBox="0 0 52 54"><polygon points="26,2 49,14 49,40 26,52 3,40 3,14" fill="#fff" stroke="#dfe4ec"/><circle cx="26" cy="27" r="9" fill="none" stroke="#0f2c6b" stroke-width="1.5"/><circle cx="26" cy="27" r="4" fill="none" stroke="#0f2c6b" stroke-width="1.5"/></svg>
        <h3 class="svc-title">Cabling Services</h3>
        <ul class="svc-list">
          <li><svg class="tick" viewBox="0 0 10 10"><circle cx="5" cy="5" r="5" fill="#0f2c6b"/><path d="M2.7 5.2 4.3 6.7 7.3 3.5" stroke="#fff" stroke-width="1.3" fill="none"/></svg>Low Voltage Wiring and Cabling</li>
          <li><svg class="tick" viewBox="0 0 10 10"><circle cx="5" cy="5" r="5" fill="#0f2c6b"/><path d="M2.7 5.2 4.3 6.7 7.3 3.5" stroke="#fff" stroke-width="1.3" fill="none"/></svg>Voice and Data Network Cabling</li>
          <li><svg class="tick" viewBox="0 0 10 10"><circle cx="5" cy="5" r="5" fill="#0f2c6b"/><path d="M2.7 5.2 4.3 6.7 7.3 3.5" stroke="#fff" stroke-width="1.3" fill="none"/></svg>CAT 3/5/6, Fiber Optic, and Coax Cabling</li>
          <li><svg class="tick" viewBox="0 0 10 10"><circle cx="5" cy="5" r="5" fill="#0f2c6b"/><path d="M2.7 5.2 4.3 6.7 7.3 3.5" stroke="#fff" stroke-width="1.3" fill="none"/></svg>Single and Multiple Floor Installations</li>
        </ul>
        <span class="outline-btn">LEARN MORE</span>
      </div>
      <div class="svc svc--left" style="top:328px">
        <div class="svc-frame"></div>
        <div class="svc-photo ph-rack" role="img" aria-label="Blue network cables plugged into a server rack"></div>
        <svg class="svc-hex" viewBox="0 0 52 54"><polygon points="26,2 49,14 49,40 26,52 3,40 3,14" fill="#fff" stroke="#dfe4ec"/><path d="M20 34V24a6 6 0 0 1 12 0v10" fill="none" stroke="#0f2c6b" stroke-width="1.5"/></svg>
        <h3 class="svc-title">Wiring Services</h3>
        <ul class="svc-list">
          <li><svg class="tick" viewBox="0 0 10 10"><circle cx="5" cy="5" r="5" fill="#0f2c6b"/><path d="M2.7 5.2 4.3 6.7 7.3 3.5" stroke="#fff" stroke-width="1.3" fill="none"/></svg>Server Racks/Networking Setup</li>
          <li><svg class="tick" viewBox="0 0 10 10"><circle cx="5" cy="5" r="5" fill="#0f2c6b"/><path d="M2.7 5.2 4.3 6.7 7.3 3.5" stroke="#fff" stroke-width="1.3" fill="none"/></svg>Audio/Video Cabling and Wiring</li>
          <li><svg class="tick" viewBox="0 0 10 10"><circle cx="5" cy="5" r="5" fill="#0f2c6b"/><path d="M2.7 5.2 4.3 6.7 7.3 3.5" stroke="#fff" stroke-width="1.3" fill="none"/></svg>WiFi - Wireless Network Installation</li>
          <li><svg class="tick" viewBox="0 0 10 10"><circle cx="5" cy="5" r="5" fill="#0f2c6b"/><path d="M2.7 5.2 4.3 6.7 7.3 3.5" stroke="#fff" stroke-width="1.3" fill="none"/></svg>Access Point Installation</li>
        </ul>
        <span class="outline-btn">LEARN MORE</span>
      </div>
      <div class="svc svc--right" style="top:547px">
        <div class="svc-frame"></div>
        <div class="svc-photo ph-city" role="img" aria-label="Night city with glowing network connection lines"></div>
        <svg class="svc-hex" viewBox="0 0 52 54"><polygon points="26,2 49,14 49,40 26,52 3,40 3,14" fill="#fff" stroke="#dfe4ec"/><circle cx="26" cy="27" r="4" fill="none" stroke="#0f2c6b" stroke-width="1.5"/><circle cx="17" cy="19" r="3" fill="none" stroke="#0f2c6b" stroke-width="1.3"/><circle cx="35" cy="19" r="3" fill="none" stroke="#0f2c6b" stroke-width="1.3"/><circle cx="17" cy="35" r="3" fill="none" stroke="#0f2c6b" stroke-width="1.3"/><circle cx="35" cy="35" r="3" fill="none" stroke="#0f2c6b" stroke-width="1.3"/></svg>
        <h3 class="svc-title">Networking Service</h3>
        <ul class="svc-list">
          <li><svg class="tick" viewBox="0 0 10 10"><circle cx="5" cy="5" r="5" fill="#0f2c6b"/><path d="M2.7 5.2 4.3 6.7 7.3 3.5" stroke="#fff" stroke-width="1.3" fill="none"/></svg>Voice &amp; Telephone Wiring</li>
          <li><svg class="tick" viewBox="0 0 10 10"><circle cx="5" cy="5" r="5" fill="#0f2c6b"/><path d="M2.7 5.2 4.3 6.7 7.3 3.5" stroke="#fff" stroke-width="1.3" fill="none"/></svg>Demarc Extension</li>
          <li><svg class="tick" viewBox="0 0 10 10"><circle cx="5" cy="5" r="5" fill="#0f2c6b"/><path d="M2.7 5.2 4.3 6.7 7.3 3.5" stroke="#fff" stroke-width="1.3" fill="none"/></svg>Security Camera Installation</li>
          <li><svg class="tick" viewBox="0 0 10 10"><circle cx="5" cy="5" r="5" fill="#0f2c6b"/><path d="M2.7 5.2 4.3 6.7 7.3 3.5" stroke="#fff" stroke-width="1.3" fill="none"/></svg>Heat Mapping</li>
        </ul>
        <span class="outline-btn">LEARN MORE</span>
      </div>
    </section>

    <section class="trust on-dark">
      <h2 class="h2">OUR TRUST</h2>
      <p class="trust-copy">WE ARE COMMITTED TO BUILDING TRUST AMONG OUR CLIENTS, CONTRACTORS,<br>COLLEAGUES, AND COMMUNITY</p>
    </section>

    <section class="markets">
      <h2 class="h2">OUR MARKETS</h2>
      <div class="card c1 r1"><div class="card-photo ph-cam" role="img" aria-label="Hands installing a security camera"></div><h4 class="card-title">RESIDENTIAL</h4><p class="card-copy">Let us assist you with your project! No project is to big or small.</p><span class="card-link">LEARN MORE</span></div>
      <div class="card c2 r1"><div class="card-photo ph-mall" role="img" aria-label="Busy shopping mall interior"></div><h4 class="card-title">COMMERCIAL</h4><p class="card-copy">Ridgewellcore is a leading services provider for Fortune 500 businesses with multiple locations</p><span class="card-link">LEARN MORE</span></div>
      <div class="card c3 r1"><div class="card-photo ph-dome" role="img" aria-label="Capitol dome under blue sky"></div><h4 class="card-title">FEDERAL</h4><p class="card-copy">We are a trusted provider for the U.S. Government with proven past performance.</p><span class="card-link">LEARN MORE</span></div>
      <div class="card c1 r2"><div class="card-photo ph-retail" role="img" aria-label="Brick retail storefront buildings"></div><h4 class="card-title">RETAIL</h4><p class="card-copy">Ridgewellcore has a vast amount of experience as a retail contractor.</p><span class="card-link">LEARN MORE</span></div>
      <div class="card c2 r2"><div class="card-photo ph-servers" role="img" aria-label="Data center aisle between server racks"></div><h4 class="card-title">DATA CENTERS</h4><p class="card-copy">Upper Management has a substantial experience in the telecommunications field.</p><span class="card-link">LEARN MORE</span></div>
      <div class="card c3 r2"><div class="card-photo ph-mixed" role="img" aria-label="Mixed-use brick apartment building"></div><h4 class="card-title">MIXED-USE</h4><p class="card-copy">Ridgewellcore's experience has been involved with mixed-use structures that typically house a variety of tenant</p><span class="card-link">LEARN MORE</span></div>
      <span class="pill">VIEW ALL</span>
    </section>

    <footer class="site-footer">© Copyrights 2021 Ridgewellcore &nbsp;|&nbsp; All Rights Reserved</footer>
  </div>

  <!-- Layout B -->
  <div class="page page--b">
    <header class="site-header">
      <div class="brand"><span class="brand-dot"></span><span class="brand-name">RIDGEWELLCORE</span></div>
      <nav class="nav"><a class="active">HOME</a><a>LOW VOLTAGE</a><a>MARKETS</a><a>OUR TEAM</a><a>CONTACT US</a></nav>
      <div class="phone"><span class="phone-ic"><svg width="10" height="10" viewBox="0 0 24 24"><path fill="#0f2c6b" d="M6.6 10.8a15.1 15.1 0 0 0 6.6 6.6l2.2-2.2c.3-.3.7-.4 1-.2 1.1.4 2.3.6 3.6.6.6 0 1 .4 1 1V20c0 .6-.4 1-1 1A17 17 0 0 1 3 4c0-.6.4-1 1-1h3.5c.6 0 1 .4 1 1 0 1.3.2 2.5.6 3.6.1.3 0 .7-.2 1z"/></svg></span>555-014-2270</div>
    </header>

    <section class="hero">
      <div class="hero-photo ph-hero" role="img" aria-label="City skyline in soft blue haze with a network of hexagon photo tiles"></div>
      <svg class="arrow" style="left:14px" width="10" height="14" viewBox="0 0 10 14"><path d="M8 1 2 7l6 6" stroke="#fff" stroke-width="2" fill="none"/></svg>
      <svg class="arrow" style="left:647px" width="10" height="14" viewBox="0 0 10 14"><path d="M2 1l6 6-6 6" stroke="#fff" stroke-width="2" fill="none"/></svg>
      <h1 class="hero-title">WITH OVER 20 YEARS OF<br>PROVEN EXPERIENCE</h1>
      <p class="hero-copy">We offer an end-to-end client experience that includes seamless communication, budgeting, staffing, on-site organization, and solid, quality handiwork every time.</p>
      <span class="pill">GET STARTED</span>
    </section>

    <section class="about">
      <h2 class="h2">ABOUT RIDGEWELLCORE</h2>
      <p class="about-copy">Lorem ipsum dolor sit amet, consectetur adipiscing elit, sed do eiusmod tempor incididunt ut labore et dolore magna aliqua. Ut enim ad minim veniam, quis nostrud exercitation ullamco laboris nisi ut aliquip ex ea commodo consequat. Duis aute irure dolor in reprehenderit in voluptate velit esse cillum dolore eu fugiat nulla pariatur. Excepteur sint occaecat cupidatat non proident, sunt in culpa qui officia deserunt mollit anim id est laborum sit amet, consectetur adipiscing elit, sed do eiusmod tempor incididunt ut labore et dolore magna aliqua. Ut enim ad minim veniam, quis nostrud exercitation ullamco laboris nisi ut aliquip ex ea commodo consequat. Duis aute irure dolor in reprehenderit in voluptate velit esse cillum dolore eu fugiat nulla pariatur.</p>
      <span class="pill">LEARN MORE</span>
    </section>

    <section class="services">
      <h2 class="h2">WHAT WE DO</h2>
      <div class="svc svc--right" style="top:109px">
        <div class="svc-frame"></div>
        <div class="svc-photo ph-panel" role="img" aria-label="Technician testing an electrical panel with a clamp meter"></div>
        <svg class="svc-hex" viewBox="0 0 52 54"><polygon points="26,2 49,14 49,40 26,52 3,40 3,14" fill="#fff" stroke="#dfe4ec"/><circle cx="26" cy="27" r="9" fill="none" stroke="#0f2c6b" stroke-width="1.5"/><circle cx="26" cy="27" r="4" fill="none" stroke="#0f2c6b" stroke-width="1.5"/></svg>
        <h3 class="svc-title">Cabling Services</h3>
        <ul class="svc-list">
          <li><svg class="tick" viewBox="0 0 10 10"><circle cx="5" cy="5" r="5" fill="#0f2c6b"/><path d="M2.7 5.2 4.3 6.7 7.3 3.5" stroke="#fff" stroke-width="1.3" fill="none"/></svg>Low Voltage Wiring and Cabling</li>
          <li><svg class="tick" viewBox="0 0 10 10"><circle cx="5" cy="5" r="5" fill="#0f2c6b"/><path d="M2.7 5.2 4.3 6.7 7.3 3.5" stroke="#fff" stroke-width="1.3" fill="none"/></svg>Voice and Data Network Cabling</li>
          <li><svg class="tick" viewBox="0 0 10 10"><circle cx="5" cy="5" r="5" fill="#0f2c6b"/><path d="M2.7 5.2 4.3 6.7 7.3 3.5" stroke="#fff" stroke-width="1.3" fill="none"/></svg>CAT 3/5/6, Fiber Optic, and Coax Cabling</li>
          <li><svg class="tick" viewBox="0 0 10 10"><circle cx="5" cy="5" r="5" fill="#0f2c6b"/><path d="M2.7 5.2 4.3 6.7 7.3 3.5" stroke="#fff" stroke-width="1.3" fill="none"/></svg>Single and Multiple Floor Installations</li>
        </ul>
        <span class="outline-btn">LEARN MORE</span>
      </div>
      <div class="svc svc--left" style="top:328px">
        <div class="svc-frame"></div>
        <div class="svc-photo ph-rack" role="img" aria-label="Blue network cables plugged into a server rack"></div>
        <svg class="svc-hex" viewBox="0 0 52 54"><polygon points="26,2 49,14 49,40 26,52 3,40 3,14" fill="#fff" stroke="#dfe4ec"/><path d="M20 34V24a6 6 0 0 1 12 0v10" fill="none" stroke="#0f2c6b" stroke-width="1.5"/></svg>
        <h3 class="svc-title">Wiring Services</h3>
        <ul class="svc-list">
          <li><svg class="tick" viewBox="0 0 10 10"><circle cx="5" cy="5" r="5" fill="#0f2c6b"/><path d="M2.7 5.2 4.3 6.7 7.3 3.5" stroke="#fff" stroke-width="1.3" fill="none"/></svg>Server Racks/Networking Setup</li>
          <li><svg class="tick" viewBox="0 0 10 10"><circle cx="5" cy="5" r="5" fill="#0f2c6b"/><path d="M2.7 5.2 4.3 6.7 7.3 3.5" stroke="#fff" stroke-width="1.3" fill="none"/></svg>Audio/Video Cabling and Wiring</li>
          <li><svg class="tick" viewBox="0 0 10 10"><circle cx="5" cy="5" r="5" fill="#0f2c6b"/><path d="M2.7 5.2 4.3 6.7 7.3 3.5" stroke="#fff" stroke-width="1.3" fill="none"/></svg>WiFi - Wireless Network Installation</li>
          <li><svg class="tick" viewBox="0 0 10 10"><circle cx="5" cy="5" r="5" fill="#0f2c6b"/><path d="M2.7 5.2 4.3 6.7 7.3 3.5" stroke="#fff" stroke-width="1.3" fill="none"/></svg>Access Point Installation</li>
        </ul>
        <span class="outline-btn">LEARN MORE</span>
      </div>
      <div class="svc svc--right" style="top:547px">
        <div class="svc-frame"></div>
        <div class="svc-photo ph-city" role="img" aria-label="Night city with glowing network connection lines"></div>
        <svg class="svc-hex" viewBox="0 0 52 54"><polygon points="26,2 49,14 49,40 26,52 3,40 3,14" fill="#fff" stroke="#dfe4ec"/><circle cx="26" cy="27" r="4" fill="none" stroke="#0f2c6b" stroke-width="1.5"/><circle cx="17" cy="19" r="3" fill="none" stroke="#0f2c6b" stroke-width="1.3"/><circle cx="35" cy="19" r="3" fill="none" stroke="#0f2c6b" stroke-width="1.3"/><circle cx="17" cy="35" r="3" fill="none" stroke="#0f2c6b" stroke-width="1.3"/><circle cx="35" cy="35" r="3" fill="none" stroke="#0f2c6b" stroke-width="1.3"/></svg>
        <h3 class="svc-title">Networking Service</h3>
        <ul class="svc-list">
          <li><svg class="tick" viewBox="0 0 10 10"><circle cx="5" cy="5" r="5" fill="#0f2c6b"/><path d="M2.7 5.2 4.3 6.7 7.3 3.5" stroke="#fff" stroke-width="1.3" fill="none"/></svg>Voice &amp; Telephone Wiring</li>
          <li><svg class="tick" viewBox="0 0 10 10"><circle cx="5" cy="5" r="5" fill="#0f2c6b"/><path d="M2.7 5.2 4.3 6.7 7.3 3.5" stroke="#fff" stroke-width="1.3" fill="none"/></svg>Demarc Extension</li>
          <li><svg class="tick" viewBox="0 0 10 10"><circle cx="5" cy="5" r="5" fill="#0f2c6b"/><path d="M2.7 5.2 4.3 6.7 7.3 3.5" stroke="#fff" stroke-width="1.3" fill="none"/></svg>Security Camera Installation</li>
          <li><svg class="tick" viewBox="0 0 10 10"><circle cx="5" cy="5" r="5" fill="#0f2c6b"/><path d="M2.7 5.2 4.3 6.7 7.3 3.5" stroke="#fff" stroke-width="1.3" fill="none"/></svg>Heat Mapping</li>
        </ul>
        <span class="outline-btn">LEARN MORE</span>
      </div>
    </section>

    <section class="trust on-dark">
      <h2 class="h2">OUR TRUST</h2>
      <p class="trust-copy">WE ARE COMMITTED TO BUILDING TRUST AMONG OUR CLIENTS, CONTRACTORS,<br>COLLEAGUES, AND COMMUNITY</p>
    </section>

    <section class="markets">
      <h2 class="h2">OUR MARKETS</h2>
      <div class="card c1 r1"><div class="card-photo ph-cam" role="img" aria-label="Hands installing a security camera"></div><h4 class="card-title">RESIDENTIAL</h4><p class="card-copy">Let us assist you with your project! No project is to big or small.</p><span class="card-link">LEARN MORE</span></div>
      <div class="card c2 r1"><div class="card-photo ph-mall" role="img" aria-label="Busy shopping mall interior"></div><h4 class="card-title">COMMERCIAL</h4><p class="card-copy">Ridgewellcore is a leading services provider for Fortune 500 businesses with multiple locations</p><span class="card-link">LEARN MORE</span></div>
      <div class="card c3 r1"><div class="card-photo ph-dome" role="img" aria-label="Capitol dome under blue sky"></div><h4 class="card-title">FEDERAL</h4><p class="card-copy">We are a trusted provider for the U.S. Government with proven past performance.</p><span class="card-link">LEARN MORE</span></div>
      <div class="card c1 r2"><div class="card-photo ph-retail" role="img" aria-label="Brick retail storefront buildings"></div><h4 class="card-title">RETAIL</h4><p class="card-copy">Ridgewellcore has a vast amount of experience as a retail contractor.</p><span class="card-link">LEARN MORE</span></div>
      <div class="card c2 r2"><div class="card-photo ph-servers" role="img" aria-label="Data center aisle between server racks"></div><h4 class="card-title">DATA CENTERS</h4><p class="card-copy">Upper Management has a substantial experience in the telecommunications field.</p><span class="card-link">LEARN MORE</span></div>
      <div class="card c3 r2"><div class="card-photo ph-mixed" role="img" aria-label="Mixed-use brick apartment building"></div><h4 class="card-title">MIXED-USE</h4><p class="card-copy">Ridgewellcore's experience has been involved with mixed-use structures that typically house a variety of tenant</p><span class="card-link">LEARN MORE</span></div>
      <span class="pill">VIEW ALL</span>
    </section>

    <footer class="site-footer">© Copyrights 2021 Ridgewellcore &nbsp;|&nbsp; All Rights Reserved</footer>
  </div>

</div>
</body>
</html>
```